Website to design and sell sundials: www.gnomonvale.com

We have a website that creates a free paper sundial, we want to migrate from this not profit free website to a website where we will continue offering the free paper sundial model but We will also offer a manufactured sundial and sell it.
In order to understand the project, please visit:
http://www.gnomonvale.com/vertical/sundial.html and
http://www.korvel.net/landing/

The website user journey should be redesigned, including the phases that are,
select language
Show product give info
Creation/edit sundial (could be one or more phases)
View created sundial
Buy sundial.

May some of them could be combined or splitted, what It have more sense.

Number of Pages Required

4 page

Font styles to use
Sans Serif

Requirements
Must have
• A description page user journey offering freemium paper sundial and physical sundial to sell.
• A sundial creation page for "free" paper sundial
• A result page for paper sundial
• A sell page for physical

```html
<!DOCTYPE html>
<html lang="en">
<head>
<meta charset="utf-8">
<title>GnomonVale – Sundials</title>
<link href="https://fonts.googleapis.com/css2?family=Roboto:wght@300;400;500;700&display=swap" rel="stylesheet">
<style>
:root{
  --red:#c0100f;
  --orange:#f7a823;
  --orange-deep:#e8860c;
  --cream:#fdf3e2;
  --beige:#f3dfbf;
  --ink:#333333;
  --grey:#8a8a8a;
  --white:#ffffff;
}
*{margin:0;padding:0;box-sizing:border-box}
html,body{width:1200px;height:2605px;overflow:hidden;background:var(--white)}
body{position:relative;font-family:'Roboto',Arial,sans-serif;color:var(--ink)}
.abs{position:absolute}
a{color:inherit;text-decoration:none}
ul,ol{list-style:none}

/* hero */
.hero{left:0;top:0;width:1200px;height:594px;
  background:
    radial-gradient(circle at 9% 2%,#fff3c8 0,#ffb15e 6%,rgba(230,80,40,.85) 14%,transparent 32%),
    radial-gradient(circle at 12% 34%,rgba(255,60,30,.75) 0,transparent 9%),
    radial-gradient(ellipse 22% 30% at 40% 38%,#f3e2b8 0,#d9b06a 25%,#a9733a 55%,transparent 100%),
    radial-gradient(ellipse 30% 40% at 38% 40%,rgba(120,70,30,.6) 0,transparent 100%),
    linear-gradient(100deg,#7a3d25 0,#94502f 25%,#6e3a24 45%,#8b4a2c 60%,#5c2f1e 78%,#7b4328 100%),
    #6e3a24}
.lang{left:1000px;top:14px;width:101px;height:24px;background:var(--orange);border-radius:5px;font-size:12px;color:var(--white);padding:5px 0 0 14px}
.lang svg{position:absolute;right:12px;top:9px}
.navbar{left:100px;top:56px;width:1001px;height:76px;background:rgba(255,255,255,.85);border-radius:10px}
.brand{left:30px;top:25px;display:flex;align-items:center;gap:10px;font-size:22px;font-weight:500;color:var(--red)}
.brand i{display:block;width:18px;height:18px;border-radius:50%;background:var(--red)}
.nav a{position:absolute;top:32px;font-size:13px;color:#666;letter-spacing:.3px}
.nav a.active{color:var(--red)}
.hero-title{left:761px;top:308px;font-size:38px;font-weight:500;color:var(--white);letter-spacing:.5px}
.hero-text{left:762px;top:356px;width:350px;font-size:13px;line-height:20px;color:var(--white)}
.arrow{width:44px;height:44px;border:2px solid rgba(255,255,255,.7);border-radius:50%;top:351px}

/* intro */
.intro{left:0;top:594px;width:1200px;height:700px;background:var(--cream)}
.mark{width:18px;height:18px;border-radius:50%;background:var(--red)}
.sec-title{width:1200px;left:0;text-align:center;font-size:24px;font-weight:500;color:var(--ink)}
.rule{height:3px;width:62px;left:569px;background:var(--orange)}
.intro-text{left:146px;top:740px;width:908px;text-align:center;font-size:11px;line-height:22px;color:var(--grey)}
.disc{width:306px;height:306px;border-radius:50%;border:3px solid var(--white);box-shadow:0 0 0 1px #e5d6bf;top:845px}
.badge{width:138px;height:138px;border-radius:50%;background:var(--white);top:1060px;display:flex;align-items:center;justify-content:center;text-align:center;font-size:17px;color:var(--red);line-height:22px;box-shadow:0 2px 6px rgba(0,0,0,.08)}
.chev{top:970px;width:20px;height:70px}

/* steps */
.steps-bg{left:0;top:1170px;width:1200px;height:471px}
.build{left:99px;top:1310px;font-size:22px;color:#111;text-decoration:underline}
.steps{left:99px;top:1370px;width:500px;font-size:13px;color:#222;line-height:16px}
.steps li{margin-bottom:12px;padding-left:12px;text-indent:-12px}
.steps b{font-weight:400;text-transform:uppercase}
.steps span{font-size:11px}
.buy{left:99px;top:1556px;width:111px;height:35px;background:#111;color:var(--white);font-size:11px;font-weight:500;border-radius:4px;display:flex;align-items:center;justify-content:center}
.feature{left:643px;top:1315px;width:458px;height:277px;border:3px solid var(--white);
  background:
    radial-gradient(ellipse 34% 28% at 42% 68%,#3e3f3f 0,#55585a 60%,transparent 100%),
    linear-gradient(180deg,#9fb6c6 0,#b9c9d2 14%,#6f8a5a 22%,#5e7750 30%,#8d9094 40%,#7d7e7c 70%,#6a6a68 100%)}

/* info boxes */
.box{top:1700px;width:316px;height:226px;background:#fdf7ee;border:1px solid #f1e4cd}
.box h3{height:52px;padding:17px 0 0 30px;font-size:18px;font-weight:500;color:var(--white);background:var(--orange)}
.box.todo h3{background:var(--red)}
.box ul{padding:22px 20px 0 30px}
.box li{position:relative;padding-left:22px;font-size:13px;color:#444;line-height:21px;margin-bottom:10px}
.box li svg{position:absolute;left:0;top:5px}

/* products */
.prod{top:2087px;width:240px;height:167px;border:8px solid var(--beige)}
.dot{top:2297px;width:12px;height:12px;border-radius:50%;background:#f6cfd0}
.dot.on{background:var(--orange)}

/* footer */
.foot{left:0;top:2250px;width:1200px;height:355px}
.f-title{top:2392px;font-size:17px;font-weight:500;color:var(--white)}
.f-links{top:2438px;font-size:11px;color:var(--white);line-height:21px}
.f-sub{left:299px;top:2420px;font-size:10px;color:var(--white)}
.email{left:299px;top:2445px;width:205px;height:35px;background:var(--white);font-size:11px;color:#aaa;padding:11px 0 0 10px}
.go{left:504px;top:2445px;width:40px;height:35px;background:#222;color:var(--white);font-size:16px;font-weight:700;display:flex;align-items:center;justify-content:center}
.divider{top:2380px;width:1px;height:155px;background:rgba(255,255,255,.25)}
.f-row{display:flex;align-items:center;gap:12px;font-size:12px;color:var(--white);height:24px}
.f-social .f-row{font-size:11px;height:25px}
.circ{width:10px;height:10px;border-radius:50%;background:var(--white)}
.copy{left:0;top:2553px;width:1200px;text-align:center;font-size:11px;color:var(--white)}
</style>
</head>
<body>

<!-- hero -->
<div class="abs hero" role="img" aria-label="Brass pocket sundial compass lying on weathered wood, warm sunlight from top left"></div>
<div class="abs lang">English
  <svg width="9" height="6" viewBox="0 0 9 6"><path d="M0 0h9L4.5 6z" fill="#fff"/></svg>
</div>
<header class="abs navbar">
  <a class="abs brand" href="#"><i></i>GnomonVale</a>
  <nav class="nav">
    <a class="active" style="left:494px">HOME</a>
    <a style="left:588px">INTODUCTION</a>
    <a style="left:730px">PRODUCT INFO</a>
    <a style="left:881px">CONTACT US</a>
  </nav>
</header>
<h1 class="abs hero-title">GNOMONVALE</h1>
<p class="abs hero-text">There are many variations of passages of available, but the majority have suffered alteration in some form, by injected humour, or randomised words.</p>
<div class="abs arrow" style="left:51px"><svg width="40" height="40" viewBox="0 0 40 40"><path d="M23 13l-7 7 7 7" stroke="#fff" stroke-width="2.5" fill="none"/></svg></div>
<div class="abs arrow" style="left:1104px"><svg width="40" height="40" viewBox="0 0 40 40"><path d="M17 13l7 7-7 7" stroke="#fff" stroke-width="2.5" fill="none"/></svg></div>

<!-- introduction -->
<section class="abs intro"></section>
<div class="abs mark" style="left:591px;top:645px"></div>
<h2 class="abs sec-title" style="top:680px">INTRODUCTION</h2>
<div class="abs rule" style="top:714px"></div>
<p class="abs intro-text">This page is about Sundials. Sundials are instruments that tell you the time with the shadow of the sun. To design a sundial you need to know exactly where you are going to put it, i.e. you need to know the longitude, the latitude and the orientation of the wall with respect to North. I have designed this page and integrated an online map. It helps you to easily find all the parameters needed and finally produces a printable page with a cut-out paper sundial, that can be cut and folded to give you a vertical sundial.</p>

<svg class="abs chev" style="left:62px" viewBox="0 0 20 70"><path d="M18 2L3 35l15 33" stroke="#e8d8be" stroke-width="2" fill="none"/></svg>
<svg class="abs chev" style="left:1118px" viewBox="0 0 20 70"><path d="M2 2l15 33-15 33" stroke="#e8d8be" stroke-width="2" fill="none"/></svg>

<div class="abs disc" style="left:99px;background:radial-gradient(ellipse 40% 26% at 55% 48%,#eef0f2 0,#d8dadd 55%,transparent 100%),linear-gradient(180deg,#9c5a48 0,#b0705c 30%,#8e4c3c 70%,#5a3a30 100%)" role="img" aria-label="Paper sundial cut out and folded against a brick wall"></div>
<div class="abs disc" style="left:446px;background:radial-gradient(ellipse 36% 24% at 50% 40%,#d9c7a6 0,#bca886 60%,transparent 100%),linear-gradient(180deg,#e6ecf0 0,#c6d0d6 35%,#6f767a 70%,#3e4244 100%)" role="img" aria-label="Vertical paper sundial fixed on a window"></div>
<div class="abs disc" style="left:792px;background:radial-gradient(ellipse 30% 22% at 50% 42%,#c9c6bd 0,#a7a59c 60%,transparent 100%),linear-gradient(135deg,#3c4a34 0,#6b7a5a 35%,#8f8f86 55%,#4d5e3e 80%,#2f3a2a 100%)" role="img" aria-label="Aerial map view showing where the sundial is located"></div>
<div class="abs badge" style="left:183px">CUT OUT<br>PAPER</div>
<div class="abs badge" style="left:530px">VERTICAL<br>SUNDIAL</div>
<div class="abs badge" style="left:876px">SUNDIAL<br>LOCATED</div>

<!-- steps band -->
<svg class="abs steps-bg" viewBox="0 0 1200 471" role="img" aria-label="Warm orange band with a faint photo of an engraved brass sundial face">
  <defs>
    <linearGradient id="band" x1="0" y1="0" x2="1" y2="1">
      <stop offset="0" stop-color="#f09a12"/>
      <stop offset=".5" stop-color="#f3b445"/>
      <stop offset="1" stop-color="#e07e08"/>
    </linearGradient>
    <radialGradient id="dial" cx=".42" cy=".62" r=".45">
      <stop offset="0" stop-color="#c46a06" stop-opacity=".35"/>
      <stop offset="1" stop-color="#c46a06" stop-opacity="0"/>
    </radialGradient>
  </defs>
  <path d="M0 10Q560 110 1200 15V471H0Z" fill="url(#band)"/>
  <path d="M0 10Q560 110 1200 15V471H0Z" fill="url(#dial)"/>
</svg>
<a class="abs build" href="#">Click here to build your custom sundial!!!</a>
<ol class="abs steps">
  <li><b>1.Calculate.</b></li>
  <li><b>2.Print the PDF.</b> <span>To print, please select "shrink to page" in order not to deform the shape of the page.</span></li>
  <li><b>3.Cut and fold:</b> <span>Once you have your model printed, you have to cut (RED LINES), and fold (BLUE LINES)</span></li>
  <li><b>4.Put on your wall.</b> <span>Put on your wall or Window</span></li>
  <li><b>5.Enjoy.</b></li>
</ol>
<a class="abs buy" href="#">BUY SUNDIAL</a>
<div class="abs feature" role="img" aria-label="Stone horizontal sundial on a paved terrace beside the sea"></div>

<!-- info boxes -->
<div class="abs box" style="left:99px">
  <h3>SUNDIAL SAMPLES</h3>
  <ul>
    <li><svg width="11" height="11" viewBox="0 0 11 11"><circle cx="5.5" cy="5.5" r="5.5" fill="#f7a823"/><path d="M4 3l2.5 2.5L4 8" stroke="#fff" stroke-width="1.5" fill="none"/></svg>South Hemisphere Buenos Aires</li>
    <li><svg width="11" height="11" viewBox="0 0 11 11"><circle cx="5.5" cy="5.5" r="5.5" fill="#f7a823"/><path d="M4 3l2.5 2.5L4 8" stroke="#fff" stroke-width="1.5" fill="none"/></svg>Valencia South east</li>
    <li><svg width="11" height="11" viewBox="0 0 11 11"><circle cx="5.5" cy="5.5" r="5.5" fill="#f7a823"/><path d="M4 3l2.5 2.5L4 8" stroke="#fff" stroke-width="1.5" fill="none"/></svg>Valencia NORTH WEST</li>
    <li><svg width="11" height="11" viewBox="0 0 11 11"><circle cx="5.5" cy="5.5" r="5.5" fill="#f7a823"/><path d="M4 3l2.5 2.5L4 8" stroke="#fff" stroke-width="1.5" fill="none"/></svg>Valencia WEST</li>
  </ul>
</div>
<div class="abs box todo" style="left:441px">
  <h3>SUNDIAL TO DO</h3>
  <ul>
    <li><svg width="11" height="11" viewBox="0 0 11 11"><circle cx="5.5" cy="5.5" r="5.5" fill="#c0100f"/><path d="M4 3l2.5 2.5L4 8" stroke="#fff" stroke-width="1.5" fill="none"/></svg>Check that all the latitudes are draw OK on the paper.</li>
    <li><svg width="11" height="11" viewBox="0 0 11 11"><circle cx="5.5" cy="5.5" r="5.5" fill="#c0100f"/><path d="M4 3l2.5 2.5L4 8" stroke="#fff" stroke-width="1.5" fill="none"/></svg>Improve explanations and webpage design</li>
  </ul>
</div>
<div class="abs box" style="left:783px">
  <h3>SUNDIAL LINKS</h3>
  <ul>
    <li><svg width="11" height="11" viewBox="0 0 11 11"><circle cx="5.5" cy="5.5" r="5.5" fill="#f7a823"/><path d="M4 3l2.5 2.5L4 8" stroke="#fff" stroke-width="1.5" fill="none"/></svg>Sundial encyclopedia page</li>
    <li><svg width="11" height="11" viewBox="0 0 11 11"><circle cx="5.5" cy="5.5" r="5.5" fill="#f7a823"/><path d="M4 3l2.5 2.5L4 8" stroke="#fff" stroke-width="1.5" fill="none"/></svg>Sundial links solvarth</li>
    <li><svg width="11" height="11" viewBox="0 0 11 11"><circle cx="5.5" cy="5.5" r="5.5" fill="#f7a823"/><path d="M4 3l2.5 2.5L4 8" stroke="#fff" stroke-width="1.5" fill="none"/></svg>The Shop for True Time</li>
    <li><svg width="11" height="11" viewBox="0 0 11 11"><circle cx="5.5" cy="5.5" r="5.5" fill="#f7a823"/><path d="M4 3l2.5 2.5L4 8" stroke="#fff" stroke-width="1.5" fill="none"/></svg>Walking shadow</li>
  </ul>
</div>

<!-- products -->
<div class="abs mark" style="left:591px;top:1970px"></div>
<h2 class="abs sec-title" style="top:2009px">SUNDIAL PRODUCT</h2>
<div class="abs rule" style="top:2043px"></div>
<div class="abs prod" style="left:99px;background:radial-gradient(ellipse 40% 44% at 45% 50%,#8a6f4c 0,#9c8462 55%,transparent 100%),linear-gradient(135deg,#d6cdbc,#b7aa92 50%,#dcd3c2)" role="img" aria-label="Octagonal bronze garden sundial on stone"></div>
<div class="abs prod" style="left:354px;background:radial-gradient(ellipse 44% 38% at 50% 50%,#f1f1f1 0,#bdbdbd 40%,#6c6c6c 75%,#2e2e2e 100%)" role="img" aria-label="Black and white human sundial with standing figures in a circle"></div>
<div class="abs prod" style="left:608px;background:radial-gradient(ellipse 40% 40% at 45% 50%,#d6a970 0,#e0bb86 50%,transparent 100%),linear-gradient(135deg,#f4e2c0,#e2c08c 50%,#f0d8ad)" role="img" aria-label="Antique paper chart of a sundial with zodiac signs"></div>
<div class="abs prod" style="left:861px;background:radial-gradient(ellipse 36% 42% at 52% 52%,#c9b57a 0,#8e9a78 45%,#5c6e66 70%,#2f383e 100%)" role="img" aria-label="Brass sundial plate with compass rose on a dark background"></div>

<!-- footer -->
<svg class="abs foot" viewBox="0 0 1200 355"><path d="M0 7Q600 160 1200 7V355H0Z" fill="#c0100f"/></svg>
<div class="abs dot" style="left:553px"></div>
<div class="abs dot on" style="left:581px"></div>
<div class="abs dot" style="left:607px"></div>
<div class="abs dot" style="left:633px"></div>

<div class="abs divider" style="left:226px"></div>
<div class="abs divider" style="left:625px"></div>
<div class="abs divider" style="left:929px"></div>

<h4 class="abs f-title" style="left:99px">HOME</h4>
<ul class="abs f-links" style="left:99px">
  <li>Home</li><li>Intoduction</li><li>Product Info</li><li>Contact US</li>
</ul>

<h4 class="abs f-title" style="left:299px">NEWSLETTER SIGN UP</h4>
<p class="abs f-sub">normal distribution of letters dfhfjgk</p>
<div class="abs email">email</div>
<div class="abs go">GO!</div>

<h4 class="abs f-title" style="left:691px">CONTACT US</h4>
<div class="abs" style="left:691px;top:2436px">
  <div class="f-row"><svg width="13" height="10" viewBox="0 0 13 10"><rect width="13" height="10" rx="1" fill="#fff"/><path d="M0 1l6.5 5L13 1" stroke="#c0100f" fill="none"/></svg>info@gnomonvale.com</div>
  <div class="f-row"><svg width="13" height="13" viewBox="0 0 13 13"><path d="M2 1l3 0 1 3-2 1.5a8 8 0 0 0 3.5 3.5L9 7l3 1v3a1.5 1.5 0 0 1-1.5 1.5A10 10 0 0 1 .5 2.5 1.5 1.5 0 0 1 2 1z" fill="#fff"/></svg>+ 555-288-0142</div>
  <div class="f-row"><svg width="13" height="13" viewBox="0 0 13 13"><rect x="3" y="0" width="7" height="4" fill="#fff"/><rect x="0" y="4" width="13" height="6" rx="1" fill="#fff"/><rect x="3" y="8" width="7" height="5" fill="#fff" stroke="#c0100f"/></svg>+ 555-865-0199</div>
</div>

<h4 class="abs f-title" style="left:1002px">FOLLOW US</h4>
<div class="abs f-social" style="left:1002px;top:2425px">
  <div class="f-row"><span class="circ"></span>FRIENDWALL</div>
  <div class="f-row"><span class="circ"></span>CHIRPLINE</div>
  <div class="f-row"><span class="circ"></span>VIDEOHALL</div>
  <div class="f-row"><span class="circ"></span>SNAPFRAME</div>
</div>

<p class="abs copy">Copyright 2015-2016. gnomonvale.com. All rights reserved.</p>

</body>
</html>
```